BOLD & MINIMALIST DESIGN NEEDED

We want a very bold but minimalistic business card design that is impactful and utilizes both sides of the business card. Our current logo is included for your use.

We want bold fonts and good use of negative space. We don't want the logo to overpower the design.

Target Market(s)

Professionals who are building new commercial buildings.

Industry/Entity Type

Construction

Contact Information for Business Card

Name, Title, email, office phone, cell phone, website

Font styles to use
Serif
Sans Serif

Requirements
Must have
• Bold design!

```html
<!DOCTYPE html>
<html lang="en">
<head>
<meta charset="utf-8">
<title>Summitline Business Card</title>
<link rel="stylesheet" href="https://fonts.googleapis.com/css2?family=Poppins:wght@400;500&display=swap">
<style>
  :root {
    --backdrop: #2b2b2b;
    --card: #262626;
    --card-light: #2e2e2e;
    --green: #7bb32e;
    --green-dark: #5f9622;
    --white: #f2f2f2;
    --ink: #1e1e1e;
  }
  html, body {
    margin: 0;
    padding: 0;
    width: 1200px;
    height: 576px;
    overflow: hidden;
    background: var(--backdrop);
    font-family: "Poppins", sans-serif;
  }
  .stage {
    position: relative;
    width: 1200px;
    height: 576px;
  }
  .card {
    position: absolute;
    top: 139px;
    height: 292px;
    border-radius: 10px;
    overflow: hidden;
    background: linear-gradient(135deg, var(--card-light), var(--card));
  }
  .card-front { left: 102px; width: 484px; }
  .card-back { left: 596px; width: 481px; }

  .brand {
    position: absolute;
    display: flex;
    align-items: center;
    gap: 10px;
    color: var(--white);
    font-weight: 500;
    letter-spacing: 1px;
    white-space: nowrap;
  }
  .brand-mark {
    background: var(--green);
    flex: none;
  }
  .card-front .brand {
    left: 50%;
    top: 50%;
    transform: translate(-50%, -50%);
    font-size: 40px;
  }
  .card-front .brand-mark { width: 30px; height: 30px; }
  .card-back .brand {
    left: 42px;
    top: 80px;
    font-size: 30px;
  }
  .card-back .brand-mark { width: 22px; height: 22px; }

  .wave {
    position: absolute;
    left: 0;
    top: 0;
    width: 481px;
    height: 292px;
  }

  .person {
    position: absolute;
    right: 26px;
    top: 29px;
    text-align: right;
  }
  .person-name {
    margin: 0;
    color: var(--green);
    font-size: 21px;
    font-weight: 500;
    line-height: 1.2;
  }
  .person-title {
    margin: 2px 0 0;
    color: var(--white);
    font-size: 12px;
    font-weight: 400;
  }

  .contact {
    position: absolute;
    right: 26px;
    top: 211px;
    margin: 0;
    padding: 0;
    list-style: none;
    color: var(--ink);
    font-size: 12px;
    line-height: 17px;
    text-align: right;
  }
  .contact li {
    display: flex;
    justify-content: flex-end;
    align-items: center;
    gap: 7px;
  }
  .contact svg {
    width: 10px;
    height: 10px;
    fill: var(--ink);
  }
</style>
</head>
<body>
<main class="stage">
  <section class="card card-front">
    <div class="brand"><span class="brand-mark"></span>SUMMITLINE</div>
  </section>

  <section class="card card-back">
    <svg class="wave" viewBox="0 0 481 292" aria-hidden="true">
      <defs>
        <linearGradient id="greenFill" x1="0" y1="0" x2="0" y2="1">
          <stop offset="0" stop-color="var(--green)"/>
          <stop offset="1" stop-color="var(--green-dark)"/>
        </linearGradient>
      </defs>
      <path d="M0,272 C120,300 220,240 300,205 C370,175 430,166 481,172 L481,292 L0,292 Z" fill="url(#greenFill)"/>
      <path d="M0,222 C60,278 160,268 240,230 C320,192 400,150 481,154 L481,166 C400,164 330,206 250,246 C170,286 60,290 0,238 Z" fill="var(--white)"/>
      <path d="M40,262 C110,282 180,270 230,252 C170,278 100,284 40,262 Z" fill="var(--white)"/>
    </svg>

    <div class="brand"><span class="brand-mark"></span>SUMMITLINE</div>

    <div class="person">
      <p class="person-name">Daniel Ferro</p>
      <p class="person-title">Director</p>
    </div>

    <ul class="contact">
      <li>555-014-0192
        <svg viewBox="0 0 10 10"><path d="M1,3 C1,1.5 9,1.5 9,3 L8,4 L6.5,3.2 L6.5,2.6 C5.5,2.3 4.5,2.3 3.5,2.6 L3.5,3.2 L2,4 Z M2.5,5 L7.5,5 L8.5,9 L1.5,9 Z"/></svg>
      </li>
      <li>mail@summitline.com
        <svg viewBox="0 0 10 10"><path d="M0.5,2 L9.5,2 L5,5.5 Z M0.5,3 L5,6.6 L9.5,3 L9.5,8.5 L0.5,8.5 Z"/></svg>
      </li>
      <li>www.summitline.com
        <svg viewBox="0 0 10 10"><circle cx="5" cy="5" r="4.5"/></svg>
      </li>
    </ul>
  </section>
</main>
</body>
</html>
```